Business Card needed for Drainor, a growing Septic Service company

Drainor, a growing local septic service company in Pennsylvania, needs updated business cards. We'd like the business card to feature our logo and communicate that we provide Septic Pumping, Installations/Repairs, Restroom Rentals, and 24/7 Emergency Service. The business card should be eye-catching, bold, and clean/simple. We have been in business almost 10 years and would like to expand and update our business brand and image.

Target Market(s)

Residential and Commercial, New and Current Homeowners

Industry/Entity Type

Service

Contact Information for Business Card

Contact on the business card should be: Dean Harlow Owner & Operator
Phone: 555-555-0187
Email: service@drainor-example.com
Website: www.drainor-example.com
Address: 812 Millbrook Lane Fernwick XY 00142

Font styles to use
Sans Serif

Colors

Designer to choose colors to be used in the design.

Requirements
Must have
• Feature logo on both side of business card.
Nice to have
• We envision the contact information on one side and our services listed on the other side. Utilize the green from the symbol in our logo as part of the design, overall design color scheme should be white, grey, black.

```html
<!DOCTYPE html>
<html lang="en">
<head>
<meta charset="utf-8">
<title>Drainor Business Card</title>
<link href="https://fonts.googleapis.com/css2?family=Raleway:wght@400;500;600;700;800&display=swap" rel="stylesheet">
<style>
  :root {
    --page: #d8d3cb;
    --card: #eef0ee;
    --ink: #2a2a2a;
    --text: #3a3a3a;
    --green: #4f8f2c;
    --green-deep: #2f7a1c;
    --ring: #f4f5f3;
    --name: #8a8a80;
    --role: #a9b2a0;
  }
  * { margin: 0; padding: 0; box-sizing: border-box; }
  html, body {
    width: 1200px; height: 969px; overflow: hidden;
    background: var(--page);
    font-family: "Raleway", sans-serif;
  }
  .card {
    position: absolute; left: 80px; top: 187px;
    width: 1040px; height: 594px;
    background: var(--card);
    border-radius: 28px;
    overflow: hidden;
    box-shadow: 0 12px 40px rgba(0,0,0,0.18);
  }
  .accent-panel {
    position: absolute; right: 0; top: 0;
    width: 480px; height: 100%;
    background: linear-gradient(90deg, rgba(79,143,44,0) 0%, rgba(79,143,44,0.75) 25%, var(--green-deep) 60%, var(--green) 100%);
  }
  .accent-disc {
    position: absolute; left: 540px; top: -70px;
    width: 480px; height: 480px; border-radius: 50%;
    background: var(--ring);
  }
  .brand {
    position: absolute; left: 66px; top: 74px;
    display: flex; align-items: center; gap: 18px;
  }
  .brand-square { width: 66px; height: 66px; background: var(--green); }
  .brand-name {
    font-weight: 800; font-size: 64px; letter-spacing: 1px;
    color: var(--ink); line-height: 1;
  }
  .contact, .services {
    position: absolute; left: 66px; list-style: none;
    font-size: 23px; color: var(--text);
  }
  .contact { top: 270px; }
  .services { top: 436px; }
  .contact li, .services li {
    display: flex; align-items: center; gap: 14px;
    height: 30px;
  }
  .icon { width: 18px; height: 18px; flex: none; }
  .bullet {
    width: 12px; height: 12px; border-radius: 50%;
    background: var(--green); margin: 0 3px; flex: none;
  }
  .person {
    position: absolute; right: 122px; top: 482px;
    text-align: right;
  }
  .person-name {
    font-weight: 700; font-size: 35px; color: var(--name); line-height: 1.1;
  }
  .person-role {
    font-weight: 400; font-size: 23px; color: var(--role);
  }
</style>
</head>
<body>
  <div class="card">
    <div class="accent-panel"></div>
    <div class="accent-disc"></div>

    <div class="brand">
      <div class="brand-square"></div>
      <div class="brand-name">DRAINOR</div>
    </div>

    <ul class="contact">
      <li>
        <svg class="icon" viewBox="0 0 24 24"><path fill="#4f8f2c" d="M6.6 10.8a15.1 15.1 0 0 0 6.6 6.6l2.2-2.2c.3-.3.7-.4 1-.2 1.1.4 2.3.6 3.6.6.6 0 1 .4 1 1V20c0 .6-.4 1-1 1A17 17 0 0 1 3 4c0-.6.4-1 1-1h3.5c.6 0 1 .4 1 1 0 1.3.2 2.5.6 3.6.1.3 0 .7-.2 1z"/></svg>
        555-555-0187
      </li>
      <li>
        <svg class="icon" viewBox="0 0 24 24"><rect x="2" y="5" width="20" height="14" fill="#4f8f2c"/><path d="M2 5l10 8 10-8" fill="none" stroke="#eef0ee" stroke-width="2"/></svg>
        service@drainor-example.com
      </li>
      <li>
        <svg class="icon" viewBox="0 0 24 24"><circle cx="12" cy="12" r="10" fill="#4f8f2c"/><path d="M2 12h20M12 2c3 3 3 17 0 20M12 2c-3 3-3 17 0 20" fill="none" stroke="#eef0ee" stroke-width="1.5"/></svg>
        www.drainor-example.com
      </li>
      <li>
        <svg class="icon" viewBox="0 0 24 24"><path fill="#4f8f2c" d="M12 2a7 7 0 0 0-7 7c0 5 7 13 7 13s7-8 7-13a7 7 0 0 0-7-7zm0 9.5a2.5 2.5 0 1 1 0-5 2.5 2.5 0 0 1 0 5z"/></svg>
        812 Millbrook Lane Fernwick XY 00142
      </li>
    </ul>

    <ul class="services">
      <li><span class="bullet"></span>Septic Pumping</li>
      <li><span class="bullet"></span>Installations/Repairs</li>
      <li><span class="bullet"></span>Restroom Rentals</li>
      <li><span class="bullet"></span>24/7 Emergency Service</li>
    </ul>

    <div class="person">
      <div class="person-name">DEAN HARLOW</div>
      <div class="person-role">Owner &amp; Operator</div>
    </div>
  </div>
</body>
</html>
```